Doctors Flyer for Workers Compensation

The purpose of the flyer is to create a handout to be used at Work Comp seminars, in order to highlight the benefits of doing workers compensation business with the doctor. The Flyer should be two sided and help to highlight the specialty of the doctor.

I have included a sample that I used for another doctor.

Industry/Entity Type

Work

Font styles to use
Serif

Requirements
Must have
• Must include a map to the practice:
• 2417 N Holloway Ave #340, Brookhaven, MO 63190
• Must Highlight the Workers Compensation Hotline: 314.555.0172
• Must Include information from information included.
• Images consistent with the Dr's specialty

```html
<!DOCTYPE html>
<html lang="en">
<head>
<meta charset="utf-8">
<title>Workers Compensation Flyer – Dr. Harwell</title>
<link href="https://fonts.googleapis.com/css2?family=Libre+Baskerville:wght@400;700&family=Open+Sans:wght@400;600;700&display=swap" rel="stylesheet">
<style>
  :root{
    --navy:#0d2f6b;
    --blue:#14509e;
    --bright:#2a7fd0;
    --sky:#8fc3ee;
    --ink:#1f3f75;
    --white:#ffffff;
    --map:#e7e4dc;
  }
  html,body{margin:0;padding:0;overflow:hidden;background:#fff;}
  .flyer{position:relative;width:885px;height:1200px;overflow:hidden;background:var(--white);font-family:"Open Sans",sans-serif;}
  .backdrop{position:absolute;inset:0;}
  .brand{position:absolute;left:480px;top:20px;display:flex;align-items:flex-start;gap:10px;}
  .brand-mark{width:22px;height:22px;border-radius:50%;background:var(--bright);margin-top:4px;}
  .brand-name{font-family:"Libre Baskerville",serif;font-weight:700;color:var(--navy);font-size:22px;line-height:1.2;}
  .photo{position:absolute;}
  .photo-doctor{left:0;top:70px;width:240px;height:310px;background:linear-gradient(180deg,#f3ece6 0%,#e8eef5 60%,#dfe7f1 100%);}
  .photo-clinic{left:240px;top:110px;width:330px;height:230px;background:linear-gradient(135deg,#dfeaf5 0%,#c9dcef 55%,#e9eef4 100%);}
  .portrait{position:absolute;left:530px;top:250px;width:200px;height:200px;border-radius:50%;border:6px solid var(--white);background:linear-gradient(180deg,#c9b7a6,#8b7665);box-sizing:border-box;}
  .headline{position:absolute;left:400px;top:470px;width:470px;text-align:center;color:var(--white);font-family:"Libre Baskerville",serif;font-size:38px;line-height:1.2;letter-spacing:1px;margin:0;font-weight:400;white-space:nowrap;}
  .section-bar{position:absolute;left:0;width:330px;height:28px;background:linear-gradient(90deg,var(--navy),var(--bright));color:var(--white);font-family:"Libre Baskerville",serif;font-weight:700;font-size:19px;line-height:28px;padding-left:22px;box-sizing:border-box;}
  .bar-hip{top:392px;}
  .bar-knee{top:720px;}
  .conditions{position:absolute;margin:0;padding:0;list-style:none;color:var(--ink);font-size:14.5px;line-height:24px;}
  .conditions li{padding-left:18px;position:relative;}
  .conditions li::before{content:"";position:absolute;left:4px;top:9px;width:6px;height:6px;background:var(--bright);}
  .list-hip{left:24px;top:430px;width:340px;}
  .list-knee-a{left:24px;top:758px;width:160px;}
  .list-knee-b{left:190px;top:758px;width:160px;}
  .map{position:absolute;left:22px;top:880px;width:320px;height:200px;background:linear-gradient(135deg,var(--map),#d5dccf);border:3px solid var(--white);box-shadow:0 0 0 1px #b8c4d4;}
  .hotline{position:absolute;left:400px;top:870px;width:470px;text-align:center;color:var(--white);}
  .hotline-label{font-family:"Libre Baskerville",serif;font-size:19px;letter-spacing:1px;line-height:1.35;margin:0;}
  .hotline-number{font-family:"Open Sans",sans-serif;font-weight:700;font-size:52px;margin:6px 0 0;letter-spacing:1px;}
  .address{position:absolute;right:36px;top:1118px;color:var(--white);font-family:"Libre Baskerville",serif;font-size:16px;letter-spacing:.5px;margin:0;white-space:nowrap;}
</style>
</head>
<body>
<div class="flyer">
  <div class="photo photo-doctor" role="img" aria-label="Smiling female doctor in a white coat with a stethoscope"></div>
  <div class="photo photo-clinic" role="img" aria-label="Doctor helping a patient during physical therapy in a bright clinic"></div>

  <svg class="backdrop" width="885" height="1200" viewBox="0 0 885 1200" aria-hidden="true">
    <defs>
      <linearGradient id="panelFill" x1="0" y1="0" x2="0" y2="1">
        <stop offset="0" stop-color="#1b5aa8"/>
        <stop offset=".45" stop-color="#0f3d82"/>
        <stop offset="1" stop-color="#0b2c63"/>
      </linearGradient>
    </defs>
    <path d="M0 70 C220 20 420 0 560 10 C420 10 230 40 0 95 Z" fill="#14509e"/>
    <path d="M0 95 C220 45 420 20 600 18 C430 30 220 70 0 118 Z" fill="#8fc3ee" opacity=".7"/>
    <path d="M885 225 C740 235 560 300 470 400 C400 480 382 570 382 660 L382 1085 L885 1085 Z" fill="url(#panelFill)"/>
    <path d="M885 225 C740 235 560 300 470 400 C400 480 382 570 382 660 L382 1085" fill="none" stroke="#8fc3ee" stroke-width="7"/>
    <path d="M0 1095 C250 1060 520 1070 885 1085 L885 1200 L0 1200 Z" fill="#0b2c63"/>
    <path d="M0 1095 C250 1060 520 1070 885 1085 L885 1098 C520 1085 250 1078 0 1110 Z" fill="#8fc3ee"/>
    <path d="M0 1170 C280 1140 560 1160 885 1150 L885 1200 L0 1200 Z" fill="#14509e"/>
  </svg>

  <div class="brand">
    <span class="brand-mark"></span>
    <span class="brand-name">Midwest Joint &amp;<br>Bone Health Center</span>
  </div>

  <div class="portrait" role="img" aria-label="Head-and-shoulders portrait of Dr. Harwell"></div>

  <h1 class="headline">CONDITIONS<br>TREATED AND<br>PROCEDURES<br>PERFORMED BY<br>DR. HARWELL</h1>

  <div class="section-bar bar-hip">HIP</div>
  <ul class="conditions list-hip">
    <li>Minimally Invasive Arthroscopic Surgery</li>
    <li>Labral Tear Repair</li>
    <li>Fractures</li>
    <li>Soft Tissue Injuries</li>
    <li>Hamstring and Quadriceps Injuries</li>
    <li>Acute Fractures in the Setting of Injury</li>
    <li>Pre-existing Avascular Necrosis</li>
    <li>Total Hip Replacement</li>
    <li>Gluteus (Buttock &amp; Hip) Muscle Repairs</li>
  </ul>

  <div class="section-bar bar-knee">KNEE</div>
  <ul class="conditions list-knee-a">
    <li>Knee Arthroscopy</li>
    <li>Ligament Injuries</li>
    <li>Meniscus Tears</li>
    <li>ACL Reconstruction</li>
  </ul>
  <ul class="conditions list-knee-b">
    <li>Cartilage Repair</li>
    <li>Cartilage Transfer</li>
    <li>Fracture Care</li>
  </ul>

  <div class="map" role="img" aria-label="Street map showing the practice at 2417 N Holloway Ave, Brookhaven"></div>

  <div class="hotline">
    <p class="hotline-label">WORKERS COMPENSATION<br>HOTLINE:</p>
    <p class="hotline-number">314.555.0172</p>
  </div>

  <p class="address">2417 N HOLLOWAY AVE #340, BROOKHAVEN, MO 63190</p>
</div>
</body>
</html>
```